Fitness competition business needs a card design

I need a professional business card design using my logo. The card will be horizontal with rounded edges.

Target Market(s)

Female fitness competitors

Industry/Entity Type

Fitness

Contact Information for Business Card

Rose-Lynn Darby
Owner
stagevarno.com
555.301.2187
info@stagevarno.com

Font styles to use
Serif

Colors

Designer to choose colors to be used in the design.

Requirements
Must have
• On the back please add the following:
• Figure
• Bikini
• Physique
• Fitness
Nice to have
• Looking for a very sleek design, contemporary and easy to read.
Should not have
• Should not be difficult to read or be too busy

```html
<!DOCTYPE html>
<html lang="en">
<head>
<meta charset="utf-8">
<title>Stage Varno – Business Card</title>
<link rel="stylesheet" href="https://fonts.googleapis.com/css2?family=Roboto+Slab:wght@400;700&display=swap">
<style>
  :root {
    --backdrop: #2b2b2c;
    --card-white: #f2f2f2;
    --brand-red: #ec1f2b;
    --ring-grey: #58585a;
    --back-grey: #5d5d5f;
    --back-mark: #6b6b6d;
    --ink-white: #ffffff;
    --ink-soft: #d9d9da;
  }
  html, body {
    margin: 0;
    padding: 0;
    width: 1200px;
    height: 960px;
    overflow: hidden;
    background: var(--backdrop);
  }
  .canvas {
    position: relative;
    width: 1200px;
    height: 960px;
  }
  .card {
    position: absolute;
    width: 600px;
    height: 343px;
    border-radius: 22px;
    overflow: hidden;
    box-shadow: 0 4px 10px rgba(0,0,0,0.45);
  }
  .card-front {
    left: 314px;
    top: 113px;
    background: var(--card-white);
  }
  .card-back {
    left: 311px;
    top: 472px;
    background: var(--back-grey);
  }
  .card-shape {
    position: absolute;
    inset: 0;
  }
  .front-brand {
    position: absolute;
    left: 30px;
    width: 226px;
    top: 186px;
    text-align: center;
    font-family: "Roboto Slab", serif;
    font-weight: 700;
    font-size: 28px;
    line-height: 34px;
    letter-spacing: 0.5px;
    color: var(--brand-red);
    margin: 0;
  }
  .contact-block {
    position: absolute;
    right: 27px;
    top: 118px;
    text-align: right;
    color: var(--ink-white);
    font-family: "Roboto Slab", serif;
  }
  .person-name {
    margin: 0;
    font-weight: 700;
    font-size: 19px;
    line-height: 24px;
    text-transform: uppercase;
  }
  .person-role {
    margin: 0 0 14px;
    font-weight: 400;
    font-size: 14px;
    line-height: 20px;
    text-transform: uppercase;
  }
  .contact-list {
    list-style: none;
    margin: 0;
    padding: 0;
    font-size: 13.5px;
    line-height: 19px;
  }
  .contact-list li {
    display: flex;
    justify-content: flex-end;
    align-items: center;
    gap: 7px;
  }
  .contact-icon {
    width: 12px;
    height: 12px;
    fill: var(--ink-white);
  }
  .back-categories {
    position: absolute;
    right: 33px;
    top: 222px;
    margin: 0;
    font-family: "Roboto Slab", serif;
    font-weight: 400;
    font-size: 12px;
    letter-spacing: 1.5px;
    color: var(--ink-soft);
    text-transform: uppercase;
  }
  .back-brand {
    position: absolute;
    right: 33px;
    top: 254px;
    margin: 0;
    font-family: "Roboto Slab", serif;
    font-weight: 700;
    font-size: 29px;
    line-height: 34px;
    color: var(--ink-white);
    letter-spacing: 0.5px;
  }
  .back-web {
    position: absolute;
    right: 31px;
    top: 306px;
    margin: 0;
    font-family: "Roboto Slab", serif;
    font-size: 13px;
    letter-spacing: 1.4px;
    color: var(--ink-white);
  }
</style>
</head>
<body>
<main class="canvas">

  <section class="card card-front" aria-label="Card front">
    <svg class="card-shape" width="600" height="343" viewBox="0 0 600 343" aria-hidden="true">
      <circle cx="465" cy="171" r="181" fill="var(--ring-grey)"/>
      <rect x="465" y="0" width="135" height="343" fill="var(--ring-grey)"/>
      <circle cx="473" cy="171" r="179" fill="var(--brand-red)" stroke="var(--ink-white)" stroke-width="2"/>
      <rect x="473" y="0" width="127" height="343" fill="var(--brand-red)"/>
    </svg>

    <p class="front-brand">STAGE VARNO</p>

    <div class="contact-block">
      <h1 class="person-name">Rose-Lynn Darby</h1>
      <p class="person-role">Owner</p>
      <ul class="contact-list">
        <li>555.301.2187
          <svg class="contact-icon" viewBox="0 0 24 24" aria-hidden="true"><path d="M6.6 10.8a15.2 15.2 0 0 0 6.6 6.6l2.2-2.2c.3-.3.7-.4 1-.2 1.1.4 2.3.6 3.6.6.6 0 1 .4 1 1V20c0 .6-.4 1-1 1A17 17 0 0 1 3 4c0-.6.4-1 1-1h3.5c.6 0 1 .4 1 1 0 1.3.2 2.5.6 3.6.1.3 0 .7-.2 1z"/></svg>
        </li>
        <li>info@stagevarno.com
          <svg class="contact-icon" viewBox="0 0 24 24" aria-hidden="true"><path d="M2 5h20v14H2z M3 6l9 7 9-7" fill="var(--ink-white)" stroke="var(--brand-red)" stroke-width="1.6"/></svg>
        </li>
        <li>stagevarno.com
          <svg class="contact-icon" viewBox="0 0 24 24" aria-hidden="true"><circle cx="12" cy="12" r="10"/><path d="M7 8c2 0 3 1 3 3s-2 2-2 4M14 5c0 2 2 2 3 4M13 19c0-2 2-3 4-3" stroke="var(--brand-red)" stroke-width="1.8" fill="none"/></svg>
        </li>
      </ul>
    </div>
  </section>

  <section class="card card-back" aria-label="Card back">
    <svg class="card-shape" width="600" height="343" viewBox="0 0 600 343" aria-hidden="true">
      <circle cx="132" cy="153" r="142" fill="var(--back-mark)"/>
    </svg>
    <p class="back-categories">Figure · Bikini · Physique · Fitness</p>
    <p class="back-brand">STAGE VARNO</p>
    <p class="back-web">www.stagevarno.com</p>
  </section>

</main>
</body>
</html>
```